Tarn - Stationary Design/Layout

We are a well established clothing design and manufacturing company (Tarn Sourcing) based in London UK, with our own factory in Bangladesh, supplying to many fashion retailers and brands. Our factory has very high environmental and ethical standards with people at its heart. Our quality of garments are second to none.
Our new logo has been proudly developed by the Pixel Guild community last month, we are now in the second phase and need the layout designed for our letterheads, double sided business cards, compliment slip and clothing ticket. Feel as creative as you like, but make sure it looks great!!
***The Logo - the logo design and colour is set and should NOT be changed and stay on a dark grey backround. The logo artwork to use is attached.
***Details to use for the business card:
Dorian Pelham
Direct Line: 020 7946 0158
dorian@tarnsourcing-example.com
Tarn Sourching Ltd.
57 - 59 Hollin Row
Camdon . Swindon
NW9 4QT
Switchboard: 020 7946 0274
Fax: 020 7946 0274
www.tarnsourcing-example.co.uk
***Details to use for the letterhead and compliment slip:
Tarn Sourching Ltd.
57 - 59 Hollin Row
Camdon . Swindon
NW9 4QT
Fax: 020 7946 0274
www.tarnsourcing-example.co.uk
***Details for Swing Ticket:
Size: 12cm height by 5.5cm width
One side need to have just the logo without the 'Sourcing', on the other it needs to stay blank

```html
<!DOCTYPE html>
<html lang="en">
<head>
<meta charset="utf-8">
<title>Tarn Sourcing – Stationery Layout</title>
<link href="https://fonts.googleapis.com/css2?family=Questrial&display=swap" rel="stylesheet">
<style>
  :root {
    --ink: #403c3c;
    --ice: #a9dde3;
    --paper: #ffffff;
    --copy: #9a9a9a;
    --line: #b9b9b9;
    --stage: #ffffff;
  }
  * { box-sizing: border-box; margin: 0; padding: 0; }
  html, body { width: 1200px; height: 900px; overflow: hidden; background: var(--stage); }
  body { position: relative; font-family: "Questrial", "Century Gothic", sans-serif; color: var(--copy); }

  .piece {
    position: absolute;
    transform: translate(-50%, -50%) rotate(var(--turn, 0deg));
    box-shadow: 2px 3px 6px rgba(0,0,0,.18);
    overflow: hidden;
  }
  .wordmark { color: var(--ice); letter-spacing: .08em; line-height: 1; font-weight: 400; }

  /* Letterhead */
  .letterhead { left: 318px; top: 386px; width: 420px; height: 594px; --turn: -16.6deg; background: var(--paper); }
  .letterhead__band { position: absolute; top: 0; left: 0; right: 0; height: 9px; background: var(--ink); }
  .letterhead__tab { position: absolute; top: 0; left: 0; width: 74px; height: 24px; background: var(--ink); padding: 9px 0 0 8px; }
  .letterhead__tab .wordmark { font-size: 14px; }
  .letterhead__body { position: absolute; top: 96px; left: 52px; right: 38px; font-size: 7.6px; line-height: 1.55; color: var(--line); }
  .letterhead__greeting { font-size: 10px; color: var(--copy); margin-bottom: 24px; }
  .letterhead__body p { margin-bottom: 12px; text-align: justify; }
  .letterhead__sign { text-align: right; margin-top: 18px; font-size: 8px; color: var(--copy); line-height: 1.3; }
  .letterhead__sign .role { font-size: 7px; }
  .letterhead__sign svg { display: block; margin: 4px 30px 0 auto; }
  .letterhead__foot { position: absolute; left: 0; bottom: 14px; padding-left: 14px; font-size: 5.6px; line-height: 1.5; color: var(--copy); border-left: 5px solid var(--ink); }
  .letterhead__foot .gap { margin-top: 8px; }
  .letterhead__foot .web { margin-top: 14px; }

  /* Business cards */
  .card { width: 172px; height: 100px; --turn: 20deg; background: var(--ink); border: 3px solid var(--ice); border-top: 0; border-right: 0; }
  .card--front { left: 502px; top: 140px; }
  .card--back { left: 566px; top: 268px; border-left: 0; border-bottom: 3px solid var(--ice); border-top: 3px solid var(--ice); }
  .card--front .wordmark { position: absolute; top: 8px; right: 10px; font-size: 12px; }
  .card__name { position: absolute; top: 12px; left: 12px; color: #fff; font-size: 8px; }
  .card__direct { position: absolute; top: 25px; left: 12px; color: #d8d8d8; font-size: 4.6px; line-height: 1.5; }
  .card__office { position: absolute; top: 25px; left: 96px; color: #d8d8d8; font-size: 4.3px; line-height: 1.45; border-left: 1px solid #6a6565; padding-left: 5px; }
  .card__web { position: absolute; bottom: 7px; right: 10px; color: #d8d8d8; font-size: 4.6px; }
  .card--back .wordmark { position: absolute; top: 38px; left: 0; right: 0; text-align: center; font-size: 20px; }

  /* Envelope */
  .envelope { left: 758px; top: 512px; width: 420px; height: 212px; --turn: -20deg; background: var(--paper); }
  .envelope__flap { position: absolute; inset: 0 0 auto 0; height: 58px; background: var(--ink); clip-path: polygon(0 100%, 9% 0, 100% 0, 100% 100%); }
  .envelope__tab { position: absolute; top: 58px; left: 0; width: 60px; height: 18px; background: var(--ink); padding: 4px 0 0 6px; }
  .envelope__tab .wordmark { font-size: 10px; }
  .envelope__window { position: absolute; right: 18px; top: 104px; width: 124px; height: 60px; border: 1px solid #8a8a8a; border-radius: 6px; background: #f4f4f4; }
  .envelope__address { position: absolute; left: 12px; bottom: 12px; font-size: 5px; line-height: 1.5; color: var(--copy); border-left: 4px solid var(--ink); padding-left: 8px; }

  /* Compliment slip */
  .slip { left: 570px; top: 722px; width: 424px; height: 196px; --turn: 10deg; background: var(--paper); }
  .slip__title { position: absolute; top: 36px; left: 24px; font-size: 11px; font-weight: 400; color: #a8a8a8; letter-spacing: .02em; }
  .slip__strip { position: absolute; top: 0; right: 0; bottom: 0; width: 48px; background: var(--ink); }
  .slip__strip .wordmark { position: absolute; top: 50%; left: 50%; transform: translate(-50%,-50%) rotate(90deg); font-size: 26px; white-space: nowrap; }
  .slip__address { position: absolute; left: 10px; bottom: 14px; font-size: 5px; line-height: 1.5; color: var(--copy); border-left: 4px solid var(--ink); padding-left: 9px; }
  .slip__address .gap { margin-top: 6px; }
  .slip__address .web { margin-top: 12px; }

  /* Swing tickets */
  .ticket { width: 78px; height: 230px; background: var(--ink); }
  .ticket--a1 { left: 858px; top: 192px; --turn: -28deg; }
  .ticket--a2 { left: 956px; top: 166px; --turn: -28deg; }
  .ticket--b1 { left: 982px; top: 432px; --turn: 17deg; }
  .ticket--b2 { left: 1085px; top: 460px; --turn: 17deg; }
  .ticket--a1 .wordmark { position: absolute; top: 50%; left: 50%; transform: translate(-50%,-50%) rotate(90deg); font-size: 34px; white-space: nowrap; }
  .ticket--b1 .wordmark { position: absolute; bottom: 12px; left: 0; right: 0; text-align: center; font-size: 20px; }

  /* Round tags */
  .tag { width: 262px; height: 108px; border-radius: 54px; background: var(--ink); --turn: -20deg; }
  .tag--front { left: 992px; top: 705px; }
  .tag--back { left: 1046px; top: 770px; }
  .tag--front .wordmark { position: absolute; top: 50%; left: 0; right: 0; transform: translateY(-50%); text-align: center; font-size: 36px; }
</style>
</head>
<body>

<article class="piece letterhead">
  <div class="letterhead__band"></div>
  <div class="letterhead__tab"><span class="wordmark">TARN</span></div>
  <div class="letterhead__body">
    <p class="letterhead__greeting">Dear Sir / Maddame</p>
    <p>Lorem ipsum dolor sit amet, consectetur adipiscing elit. Aenean ullamcorper tempor nisi, blandit ornare elit ultricies a. Sed non sem in elit tincidunt dignissim. Sed blandit mollis nisl, sed faucibus turpis feugiat convallis. Vestibulum ante ipsum primis in faucibus orci luctus et ultrices posuere cubilia curae.</p>
    <p>In ultricies convallis eleifend. Nulla ac velit sed nibh tincidunt volutpat. Donec turpis massa, rhoncus sed dignissim non, condimentum sed tortor. Quisque ipsum arcu, condimentum eu pharetra ac, tincidunt ac nibh. Nulla at convallis nibh.</p>
    <p>Vivamus luctus posuere justo, eget blandit dui porttitor ac. Nam fermentum leo id elit consectetur vel lobortis ligula eleifend. Nulla facilisi. Duis molestie viverra odio, sed pharetra ante laoreet in.</p>
    <div class="letterhead__sign">
      Alder Voss<br><span class="role">marketing director</span>
      <svg width="16" height="14" viewBox="0 0 16 14" aria-hidden="true"><path d="M2 3 C8 0 13 4 9 8 C6 11 3 9 6 7 M9 8 L12 13" fill="none" stroke="#777" stroke-width="1"/></svg>
    </div>
  </div>
  <footer class="letterhead__foot">
    <div>Tarn Sourching Ltd.</div>
    <div>57 - 59 Hollin Row . Camdon . Swindon NW9 4QT</div>
    <div class="gap">Switchboard: 020 7946 0274</div>
    <div>Fax: 020 7946 0274</div>
    <div class="web">www.tarnsourcing-example.co.uk</div>
  </footer>
</article>

<article class="piece card card--front">
  <span class="wordmark">TARN</span>
  <div class="card__name">Dorian Pelham</div>
  <div class="card__direct">Direct Line: 020 7946 0158<br>dorian@tarnsourcing-example.com</div>
  <div class="card__office">Tarn Sourching Ltd.<br>57 - 59 Hollin Row<br>Camdon . Swindon<br>NW9 4QT<br>Switchboard: 020 7946 0274<br>Fax: 020 7946 0274</div>
  <div class="card__web">www.tarnsourcing-example.co.uk</div>
</article>

<article class="piece card card--back">
  <span class="wordmark">TARN</span>
  <div class="card__web">www.tarnsourcing-example.co.uk</div>
</article>

<article class="piece envelope">
  <div class="envelope__flap"></div>
  <div class="envelope__tab"><span class="wordmark">TARN</span></div>
  <div class="envelope__window"></div>
  <div class="envelope__address">
    Tarn Sourching Ltd.<br>57 - 59 Hollin Row . Camdon . Swindon NW9 4QT<br>Switchboard: 020 7946 0274<br>Fax: 020 7946 0274
  </div>
</article>

<article class="piece slip">
  <h2 class="slip__title">With Compliments</h2>
  <div class="slip__strip"><span class="wordmark">TARN</span></div>
  <div class="slip__address">
    <div>Tarn Sourching Ltd.</div>
    <div>57 - 59 Hollin Row . Camdon . Swindon NW9 4QT</div>
    <div class="gap">Switchboard: 020 7946 0274</div>
    <div>Fax: 020 7946 0274</div>
    <div class="web">www.tarnsourcing-example.co.uk</div>
  </div>
</article>

<div class="piece ticket ticket--a1"><span class="wordmark">TARN</span></div>
<div class="piece ticket ticket--a2"></div>
<div class="piece ticket ticket--b1"><span class="wordmark">TARN</span></div>
<div class="piece ticket ticket--b2"></div>

<div class="piece tag tag--front"><span class="wordmark">TARN</span></div>
<div class="piece tag tag--back"></div>

</body>
</html>
```